Business Card Design

Carl Brennow Insurance Agency, an Independent Insurance Agency which was stated on Pellham Row in Laplace, Louisiana on 1958 and has grown the six locations throughout South Louisiana. We sell personal (auto Homeowners flood, liability) and commercial insurance (commercial property, general liability, workers compensation, commercial auto). I am looking for a double sided card with list the five remaining locations on the back or maybe even a folded four sided card. Our home office is a two story building with a green roof. I have had a logo designed which I have attached. Open for revisions but would like to stay with in the same green roof over an M. I have attached the logo but can not tell if I was uploaded.

Target Market(s)

Individual and commercial insurance buyers. Upper income and business owners

Industry/Entity Type

Insurance

Requirements
Must have
• Must have similar logo as uploaded. Green roof over M or something similar. List all location address and phone numbers.

Employee name, office phone number; direct phone line; email address and website list all locations on card. Very Similar colors to current logo.
Nice to have
• Possible folded card with double sided print

```html
<!DOCTYPE html>
<html lang="en">
<head>
<meta charset="utf-8">
<title>Carl Brennow Insurance Agency – Business Card</title>
<link rel="stylesheet" href="https://fonts.googleapis.com/css2?family=Roboto+Condensed:wght@400;700&family=Arimo:wght@400&display=swap">
<style>
  :root {
    --page-bg: #e9edf2;
    --card-white: #ffffff;
    --panel-white: rgba(255, 255, 255, 0.82);
    --brand-green: #1f5a2a;
    --brand-blue: #1f3fd6;
    --tagline-grey: #4d5a52;
    --ink: #1c1c1c;
    --icon-blue: #2a4cc9;
    --mesh-teal: #7fd6dc;
    --mesh-cyan: #9fe3e8;
    --mesh-blue: #4cb2e6;
    --mesh-deep: #2c84c8;
  }
  * { box-sizing: border-box; margin: 0; padding: 0; }
  html, body {
    width: 1200px; height: 848px; overflow: hidden;
    background: var(--page-bg);
  }
  .canvas { position: relative; width: 1200px; height: 848px; }

  .card {
    position: absolute; left: 371px; width: 478px; height: 292px;
    background: var(--card-white); overflow: hidden;
  }
  .card--front { top: 107px; }
  .card--back  { top: 491px; }

  .card__mesh {
    position: absolute; inset: 0;
    background:
      linear-gradient(180deg, rgba(255,255,255,0.92) 0%, rgba(255,255,255,0.55) 55%, rgba(255,255,255,0) 100%),
      radial-gradient(ellipse 60% 55% at 30% 100%, var(--mesh-deep) 0%, var(--mesh-teal) 45%, rgba(159,227,232,0) 100%),
      radial-gradient(ellipse 55% 70% at 100% 85%, var(--mesh-blue) 0%, var(--mesh-cyan) 50%, rgba(255,255,255,0) 100%),
      linear-gradient(180deg, #f4fbfc 0%, #d6f1f4 100%);
  }

  .card__panel { position: absolute; background: var(--panel-white); }

  /* Front */
  .card--front .card__panel { left: 49px; top: 53px; width: 326px; height: 122px; }
  .brand {
    position: absolute; left: 60px; top: 70px; width: 310px;
    display: flex; align-items: center; gap: 10px;
  }
  .brand__square { width: 52px; height: 52px; flex: none; background: var(--brand-green); }
  .brand__name {
    font-family: "Roboto Condensed", sans-serif; font-weight: 700;
    color: var(--brand-green); text-transform: uppercase; line-height: 1;
  }
  .brand__name-line1 { display: block; font-size: 27px; }
  .brand__name-line2 { display: block; font-size: 19px; margin-top: 2px; }
  .tagline {
    position: absolute; left: 122px; top: 131px;
    font-family: "Roboto Condensed", sans-serif; font-weight: 700;
    font-size: 15px; color: var(--tagline-grey); white-space: nowrap;
  }
  .locations {
    position: absolute; left: 128px; top: 152px; width: 240px;
    font-family: "Roboto Condensed", sans-serif; font-weight: 700;
    color: var(--brand-blue); text-align: center; line-height: 1.15;
  }
  .locations__intro { font-size: 7px; }
  .locations__list { font-size: 7px; white-space: nowrap; }
  .locations__town + .locations__town { margin-left: 5px; }

  /* Back */
  .card--back .card__panel { left: 49px; top: 54px; width: 326px; height: 110px; }
  .contact {
    position: absolute; left: 65px; top: 63px; list-style: none;
    font-family: "Arimo", sans-serif; font-size: 14.5px; color: var(--ink);
  }
  .contact__item { display: flex; align-items: center; gap: 10px; height: 24px; }
  .contact__icon {
    width: 16px; height: 16px; flex: none; background: var(--icon-blue);
    border-radius: 2px; display: flex; align-items: center; justify-content: center;
  }
  .contact__icon svg { width: 11px; height: 11px; fill: #fff; }
  .contact__fax { margin-left: 14px; }
</style>
</head>
<body>
<main class="canvas">

  <section class="card card--front" aria-label="Card front">
    <div class="card__mesh" role="img" aria-label="Wavy blue and teal mesh pattern"></div>
    <div class="card__panel"></div>
    <div class="brand">
      <span class="brand__square"></span>
      <h1 class="brand__name">
        <span class="brand__name-line1">Carl Brennow</span>
        <span class="brand__name-line2">Insurance Agency</span>
      </h1>
    </div>
    <p class="tagline">Serving Pellham Row Since 1958</p>
    <div class="locations">
      <p class="locations__intro">Visit one of our 6 convenient locations</p>
      <p class="locations__list"><span class="locations__town">Bayridge</span><span class="locations__town">Corwick</span><span class="locations__town">Del Marsh</span><span class="locations__town">Farrowby</span><span class="locations__town">Lindale</span><span class="locations__town">Westbrooke</span></p>
    </div>
  </section>

  <section class="card card--back" aria-label="Card back">
    <div class="card__mesh" role="img" aria-label="Wavy blue and teal mesh pattern"></div>
    <div class="card__panel"></div>
    <ul class="contact">
      <li class="contact__item">
        <span class="contact__icon"><svg viewBox="0 0 24 24"><path d="M6.6 10.8a15.1 15.1 0 0 0 6.6 6.6l2.2-2.2c.3-.3.7-.4 1-.2 1.1.4 2.3.6 3.6.6.6 0 1 .4 1 1V20c0 .6-.4 1-1 1A17 17 0 0 1 3 4c0-.6.4-1 1-1h3.5c.6 0 1 .4 1 1 0 1.3.2 2.5.6 3.6.1.3 0 .7-.2 1z"/></svg></span>
        <span>225-555-0148<span class="contact__fax">Fax: 0123456789</span></span>
      </li>
      <li class="contact__item">
        <span class="contact__icon"><svg viewBox="0 0 24 24"><path d="M12 3 2 12h3v8h5v-6h4v6h5v-8h3z"/></svg></span>
        <span>No, Street, City, Postal Code, Country</span>
      </li>
      <li class="contact__item">
        <span class="contact__icon"><svg viewBox="0 0 24 24" fill="none"><g fill="none" stroke="#fff" stroke-width="2"><circle cx="12" cy="12" r="9"/><ellipse cx="12" cy="12" rx="4" ry="9"/><path d="M3 12h18"/></g></svg></span>
        <span>www.carlbrennowinsurance.com</span>
      </li>
      <li class="contact__item">
        <span class="contact__icon"><svg viewBox="0 0 24 24"><path d="M3 5h18v14H3z M4 6l8 6 8-6" fill="none" stroke="#fff" stroke-width="2"/></svg></span>
        <span>company@name.com</span>
      </li>
    </ul>
  </section>

</main>
</body>
</html>
```